Video Production Company Website

A video production company website for "Quiet Fern Studios"
Home page must have video player and way to select between 3 different videos.

Company does video Post production : Editing, Motion Graphics, Color correction, and Aerial videography

Design should be simple but Pro looking..

Earthy color palette with slight texture..

Industry/Entity Type

Film Production

Number of Pages Required

3 page

Font styles to use
Sans Serif
Other font styles liked:

Requirements
Nice to have
• Thumbnails on homepage to past project clips
Should not have
• full page video

```html
<!DOCTYPE html>
<html lang="en">
<head>
<meta charset="utf-8">
<title>Quiet Fern Studios</title>
<link href="https://fonts.googleapis.com/css2?family=Oswald:wght@400;500&family=Crimson+Text:wght@400&family=Open+Sans:wght@400;600&display=swap" rel="stylesheet">
<style>
:root{
  --cream:#e9e3d0;
  --ink:#1c1c1a;
  --nav:#191918;
  --stage:#0f0f0e;
  --white:#ffffff;
  --sage:#3f5c4b;
  --mint:#63c596;
  --mint-dark:#4eae80;
  --muted:#8a8a86;
  --text:#333331;
}
*{margin:0;padding:0;box-sizing:border-box}
html,body{width:786px;height:1200px;overflow:hidden}
body{font-family:"Open Sans",sans-serif;background:var(--white);color:var(--text);position:relative}

.site-header{height:128px;background:var(--cream);display:flex;align-items:center;justify-content:center}
.brand{font-family:"Oswald",sans-serif;font-weight:500;font-size:38px;color:var(--ink);letter-spacing:1px;display:flex;align-items:center;gap:12px}
.brand-dot{width:14px;height:14px;border-radius:50%;background:var(--ink)}

.main-nav{height:24px;background:var(--nav);display:flex;justify-content:center;align-items:center;gap:44px}
.main-nav a{font-family:"Oswald",sans-serif;font-size:12px;letter-spacing:1.5px;color:var(--white);text-decoration:none;text-transform:uppercase}

.showcase{height:430px;background:var(--stage);padding-top:16px}
.player{width:594px;margin:0 auto}
.player-screen{height:264px;background:radial-gradient(ellipse at 50% 45%,#d9cfb4 0%,#c2b494 60%,#9c8e70 100%);border:1px solid #2a2a28}
.player-controls{height:29px;background:#1e1e1d;display:flex;align-items:center;gap:12px;padding:0 12px}
.ctrl-btn{width:14px;height:14px}
.progress{flex:1;height:6px;background:#3a3a38;position:relative}
.progress span{position:absolute;left:0;top:0;height:6px;width:6%;background:#e8e8e8}
.time{font-size:9px;color:#bdbdb8}
.clip-list{width:594px;margin:11px auto 0;display:flex;gap:8px}
.clip{flex:1;height:96px;border:3px solid #3a3a38}
.clip.is-active{border-color:#8c8c86}
.clip-1{background:linear-gradient(135deg,#d4c9ab,#a89a7a)}
.clip-2{background:linear-gradient(135deg,#4a3f6e,#2b2547)}
.clip-3{background:linear-gradient(135deg,#7fb5a3,#d9d4c8)}

.services{height:283px;text-align:center;padding-top:14px}
.section-title{font-family:"Crimson Text",serif;font-size:40px;color:var(--sage);font-weight:400;line-height:1.1}
.section-kicker{display:flex;align-items:center;justify-content:center;gap:10px;font-family:"Oswald",sans-serif;font-size:10px;letter-spacing:1.5px;color:var(--muted);text-transform:uppercase;margin-top:2px}
.section-kicker::before,.section-kicker::after{content:"";width:170px;height:1px;background:#c9c9c4}
.service-grid{display:grid;grid-template-columns:repeat(4,172px);margin:22px 0 0 50px}
.service{display:flex;flex-direction:column;align-items:center;padding:0 24px}
.service svg{width:40px;height:40px}
.service h3{font-family:"Oswald",sans-serif;font-weight:400;font-size:12px;letter-spacing:1px;text-transform:uppercase;color:var(--ink);margin-top:12px}
.service p{font-size:8.5px;line-height:1.45;color:var(--muted);margin-top:6px}
.read-more{font-size:8px;color:var(--mint-dark);margin-top:10px;text-decoration:none}

.welcome{position:absolute;left:0;top:865px;width:786px;height:335px;background:var(--mint);text-align:center;color:var(--white);padding-top:52px}
.welcome h2{font-family:"Crimson Text",serif;font-weight:400;font-size:40px;line-height:1.1}
.welcome .section-kicker{color:#eafff4;margin-top:6px}
.welcome .section-kicker::before,.welcome .section-kicker::after{background:#a9e3c6;width:150px}
.welcome p{width:600px;margin:14px auto 0;font-size:9px;line-height:1.6;color:#f2fff8}
.button{display:inline-block;margin-top:30px;border:1px solid #d9f5e7;color:var(--white);font-size:9px;padding:5px 20px;text-decoration:none}
</style>
</head>
<body>
<header class="site-header">
  <div class="brand"><span class="brand-dot"></span>Quiet Fern Studios</div>
</header>
<nav class="main-nav">
  <a href="#">Home</a><a href="#">About</a><a href="#">Services</a><a href="#">Works</a><a href="#">Request a Quote</a><a href="#">Contact</a>
</nav>

<section class="showcase">
  <div class="player">
    <div class="player-screen" role="img" aria-label="Featured video frame showing the studio title card on a warm textured background"></div>
    <div class="player-controls">
      <svg class="ctrl-btn" viewBox="0 0 14 14"><rect x="3" y="2" width="3" height="10" fill="#e8e8e8"/><rect x="8" y="2" width="3" height="10" fill="#e8e8e8"/></svg>
      <div class="progress"><span></span></div>
      <span class="time">0:04</span>
      <svg class="ctrl-btn" viewBox="0 0 14 14"><path d="M2 5h3l4-3v10l-4-3H2z" fill="#e8e8e8"/></svg>
    </div>
  </div>
  <div class="clip-list">
    <div class="clip clip-1 is-active" role="img" aria-label="Project clip thumbnail: studio title card"></div>
    <div class="clip clip-2" role="img" aria-label="Project clip thumbnail: show title on a purple background"></div>
    <div class="clip clip-3" role="img" aria-label="Project clip thumbnail: bright interior scene"></div>
  </div>
</section>

<section class="services">
  <h2 class="section-title">Our Services</h2>
  <div class="section-kicker">Our Expertise</div>
  <div class="service-grid">
    <div class="service">
      <svg viewBox="0 0 40 40"><rect x="5" y="7" width="30" height="20" rx="2" fill="none" stroke="#1c1c1a" stroke-width="3"/><path d="M17 14l7 4-7 4z" fill="#1c1c1a"/><rect x="17" y="28" width="6" height="4" fill="#1c1c1a"/><rect x="12" y="32" width="16" height="3" fill="#1c1c1a"/></svg>
      <h3>Editing</h3>
      <p>Careful cuts and pacing shape raw footage into a clear story your audience will follow from first frame to last.</p>
      <a class="read-more" href="#">Read More</a>
    </div>
    <div class="service">
      <svg viewBox="0 0 40 40"><circle cx="12" cy="9" r="5" fill="none" stroke="#1c1c1a" stroke-width="2.5"/><circle cx="24" cy="9" r="5" fill="none" stroke="#1c1c1a" stroke-width="2.5"/><rect x="6" y="15" width="24" height="12" fill="#1c1c1a"/><path d="M30 18l7-4v14l-7-4z" fill="#1c1c1a"/><path d="M14 27l-5 10M22 27l5 10" stroke="#1c1c1a" stroke-width="2.5"/></svg>
      <h3>Motion Graphics</h3>
      <p>Titles, lower thirds and animated graphics add motion and polish that help every message land with clarity and style.</p>
      <a class="read-more" href="#">Read More</a>
    </div>
    <div class="service">
      <svg viewBox="0 0 40 40"><path d="M20 4C10 4 4 11 4 19c0 9 7 15 13 15 3 0 3-3 1-5-2-2 0-5 3-5h5c6 0 10-4 10-9C36 9 29 4 20 4z" fill="#1c1c1a"/><circle cx="12" cy="17" r="2.5" fill="#fff"/><circle cx="17" cy="10" r="2.5" fill="#fff"/><circle cx="25" cy="10" r="2.5" fill="#fff"/><path d="M24 30l12-14 3 2-11 15z" fill="#1c1c1a"/></svg>
      <h3>Color Correction</h3>
      <p>Balanced tones and graded looks give each scene a consistent mood, from natural daylight to rich cinematic contrast.</p>
      <a class="read-more" href="#">Read More</a>
    </div>
    <div class="service">
      <svg viewBox="0 0 40 40"><rect x="16" y="16" width="8" height="8" fill="#1c1c1a"/><path d="M16 16L9 9M24 16l7-7M16 24l-7 7M24 24l7 7" stroke="#1c1c1a" stroke-width="2.5"/><circle cx="8" cy="8" r="5" fill="none" stroke="#1c1c1a" stroke-width="2"/><circle cx="32" cy="8" r="5" fill="none" stroke="#1c1c1a" stroke-width="2"/><circle cx="8" cy="32" r="5" fill="none" stroke="#1c1c1a" stroke-width="2"/><circle cx="32" cy="32" r="5" fill="none" stroke="#1c1c1a" stroke-width="2"/></svg>
      <h3>Aerial Photography</h3>
      <p>Licensed pilots capture sweeping views from above, adding scale and drama to events, landscapes and property tours.</p>
      <a class="read-more" href="#">Read More</a>
    </div>
  </div>
</section>

<section class="welcome">
  <h2>welcome to Quiet Fern</h2>
  <div class="section-kicker">A small description about who we are and what we do</div>
  <p>We are a small post production studio that turns footage into finished films. Our team edits, animates, grades and flies cameras for brands, events and filmmakers who care about craft. Every project gets close attention, honest timelines and a finish that looks right on any screen, from phones to the big room. We keep the process simple so you can focus on the story while we handle the details behind it.</p>
  <a class="button" href="#">Read More</a>
</section>
</body>
</html>
```